Online bill payment portal website design

Online Invoice Payment Website

The customer will click on the logos of the institution they want to pay and the payment will be made at the latest stage to write the customer number.

Invoice payment can be made online. Telephone, Television, Internet, Electricity, Water, Natural Gas, and all institutional payments.

Example website : https://www.zenitodeme.com/

Industry/Entity Type

Invoice

Logo Text

HizliBorcKapat.Net

Number of Pages Required

4 page

Font styles to use
Serif
Sans Serif

Colors
abd036
33a6d7
876aae
e667a6
ec1f27
f37122
85abd2
0555a3
00a990

Requirements
Must have
• Logos of payment institutions
• Credit Card Payment form
• Customer information form
• COntact page
• List of Institutions
• Accept privacy policies in all forms
Nice to have
• Good and new design :)
Should not have
• Same with zenitodeme.com ! i want new site

```html
<!DOCTYPE html>
<html lang="en">
<head>
<meta charset="utf-8">
<title>Company Name – Online Bill Payment</title>
<link href="https://fonts.googleapis.com/css2?family=Glegoo&family=Mada:wght@300;400;500;700&display=swap" rel="stylesheet">
<style>
  :root{
    --orange:#f37122;
    --orange-dark:#d45c12;
    --blue:#33a6d7;
    --purple:#876aae;
    --pink:#e667a6;
    --red:#ec4448;
    --teal:#20c0a6;
    --amber:#e8874a;
    --sky:#85abd2;
    --lime:#abd036;
    --green:#6fb43f;
    --forest:#1f6a4a;
    --ink:#333;
    --muted:#555;
    --page:#efefef;
    --line:#e6e6e6;
    --white:#fff;
  }
  *{box-sizing:border-box;margin:0;padding:0}
  html,body{width:1200px;height:1118px;overflow:hidden}
  body{font-family:"Mada",sans-serif;color:var(--ink);background:var(--white);position:relative}

  .site-header{height:89px;position:relative;background:var(--white)}
  .brand{position:absolute;left:74px;top:18px}
  .brand-mark{display:inline-block;width:14px;height:14px;border-radius:50%;background:var(--blue);vertical-align:middle;margin-right:6px}
  .brand-name{font-size:16px;font-weight:500;color:#111;vertical-align:middle}
  .brand-tag{display:block;font-size:7px;color:#777;margin-top:2px}
  .main-nav{position:absolute;left:697px;top:34px;display:flex;gap:22px;font-size:14px;letter-spacing:.5px;color:var(--muted)}
  .btn{position:absolute;top:28px;height:33px;width:90px;font-size:14px;letter-spacing:.5px;display:flex;align-items:center;justify-content:center;border-radius:2px}
  .btn-signup{left:936px;border:1px solid var(--blue);color:var(--blue);background:var(--white)}
  .btn-signin{left:1036px;background:var(--orange);color:var(--white)}

  .content{position:absolute;top:89px;left:0;width:1200px;height:921px;background:var(--page)}
  .section-title{font-family:"Glegoo",serif;font-size:22px;font-weight:400;text-align:center;color:#333;position:absolute;left:0;width:1200px}

  .institutions{position:absolute;left:74px;top:106px;width:1052px;display:grid;grid-template-columns:repeat(5,1fr);grid-auto-rows:148px;background:var(--white)}
  .institution{border-right:1px solid var(--line);border-bottom:1px solid var(--line);display:flex;align-items:center;justify-content:center;gap:8px;font-size:18px;font-weight:700;background:var(--white);white-space:nowrap}
  .institution:nth-child(5n){border-right:none}
  .institution.is-active{box-shadow:0 0 12px rgba(0,0,0,.15);position:relative;z-index:1}
  .dot{width:16px;height:16px;border-radius:50%;flex:none}
  .i-cloud{color:#333}.i-cloud .dot{background:#333}
  .i-spiral{color:var(--orange)}.i-spiral .dot{background:var(--orange)}
  .i-leaf{color:var(--green)}.i-leaf .dot{background:var(--green)}
  .i-wood{color:#222}.i-wood .dot{background:#222}
  .i-gas{color:var(--forest)}.i-gas .dot{background:var(--forest)}

  .categories{position:absolute;top:677px;left:57px;width:1086px;display:grid;grid-template-columns:repeat(7,1fr)}
  .category{text-align:center;border-right:1px solid #dcdcdc;height:92px}
  .category:last-child{border-right:none}
  .cat-icon{width:59px;height:59px;border-radius:50%;margin:0 auto;display:flex;align-items:center;justify-content:center}
  .cat-label{font-size:18px;color:#333;margin-top:18px;display:block}

  .search{position:absolute;top:824px;left:0;width:1200px;height:44px}
  .search-label{position:absolute;right:725px;top:10px;font-family:"Glegoo",serif;font-size:18px;white-space:nowrap}
  .search-input{position:absolute;left:496px;top:0;width:271px;height:42px;border:1px solid #d6d6d6;background:var(--white);font-family:"Mada",sans-serif;font-size:14px;color:#888;padding:12px}
  .search-btn{position:absolute;left:776px;top:0;width:124px;height:42px;background:var(--orange);color:var(--white);border:none;border-bottom:3px solid var(--orange-dark);border-radius:2px;font-family:"Mada",sans-serif;font-size:14px;letter-spacing:.5px}

  .site-footer{position:absolute;top:1010px;left:0;width:1200px;height:108px;text-align:center}
  .cards{display:flex;justify-content:center;gap:6px;margin-top:28px}
  .card{width:47px;height:29px;border-radius:3px;background:#e2e2e2}
  .copyright{font-size:15px;color:#444;margin-top:12px}
</style>
</head>
<body>
<header class="site-header">
  <div class="brand">
    <span class="brand-mark"></span><span class="brand-name">Company Name</span>
    <span class="brand-tag">Add some color to your business!</span>
  </div>
  <nav class="main-nav"><span>HOME</span><span>ABOUT</span><span>CONTACT</span></nav>
  <a class="btn btn-signup">SIGN UP</a>
  <a class="btn btn-signin">SIGN IN</a>
</header>

<main class="content">
  <h2 class="section-title" style="top:40px">Select The Institution</h2>
  <div class="institutions">
    <div class="institution i-cloud"><span class="dot"></span>Bulutfix</div>
    <div class="institution i-spiral"><span class="dot"></span>Sarmal Tel</div>
    <div class="institution i-leaf"><span class="dot"></span>Yesilhat Enerji</div>
    <div class="institution i-wood"><span class="dot"></span>Ahsapnet</div>
    <div class="institution i-gas"><span class="dot"></span>Karogaz.net</div>
    <div class="institution i-spiral"><span class="dot"></span>Sarmal Tel</div>
    <div class="institution i-wood"><span class="dot"></span>Ahsapnet</div>
    <div class="institution i-spiral is-active"><span class="dot"></span>Sarmal Tel</div>
    <div class="institution i-cloud"><span class="dot"></span>Bulutfix</div>
    <div class="institution i-spiral"><span class="dot"></span>Sarmal Tel</div>
    <div class="institution i-leaf"><span class="dot"></span>Yesilhat Enerji</div>
    <div class="institution i-cloud"><span class="dot"></span>Bulutfix</div>
    <div class="institution i-gas"><span class="dot"></span>Karogaz.net</div>
    <div class="institution i-wood"><span class="dot"></span>Ahsapnet</div>
    <div class="institution i-leaf"><span class="dot"></span>Yesilhat Enerji</div>
  </div>

  <h2 class="section-title" style="top:600px">Pay Bill Online Now!</h2>
  <div class="categories">
    <div class="category"><div class="cat-icon" style="background:var(--purple)">
      <svg width="26" height="26" viewBox="0 0 26 26" fill="none" stroke="#fff" stroke-width="1.4"><circle cx="4" cy="4" r="2.5"/><circle cx="13" cy="4" r="2.5"/><circle cx="22" cy="4" r="2.5"/><circle cx="4" cy="13" r="2.5"/><circle cx="13" cy="13" r="2.5"/><circle cx="22" cy="13" r="2.5"/><circle cx="4" cy="22" r="2.5"/><circle cx="13" cy="22" r="2.5"/><circle cx="22" cy="22" r="2.5"/></svg>
    </div><span class="cat-label">All</span></div>
    <div class="category"><div class="cat-icon" style="background:var(--pink)">
      <svg width="20" height="30" viewBox="0 0 20 30" fill="none" stroke="#fff" stroke-width="1.5"><rect x="2" y="1" width="16" height="28" rx="2"/><line x1="2" y1="6" x2="18" y2="6"/><line x1="2" y1="23" x2="18" y2="23"/><circle cx="10" cy="26" r="1"/></svg>
    </div><span class="cat-label">Telephone</span></div>
    <div class="category"><div class="cat-icon" style="background:var(--red)">
      <svg width="30" height="28" viewBox="0 0 30 28" fill="none" stroke="#fff" stroke-width="1.5"><path d="M10 2l5 5 5-5"/><rect x="2" y="7" width="26" height="17" rx="2"/><rect x="6" y="10" width="18" height="11"/><line x1="7" y1="24" x2="7" y2="27"/><line x1="23" y1="24" x2="23" y2="27"/></svg>
    </div><span class="cat-label">Television</span></div>
    <div class="category"><div class="cat-icon" style="background:var(--teal)">
      <svg width="30" height="30" viewBox="0 0 30 30" fill="none" stroke="#fff" stroke-width="1.5"><circle cx="15" cy="15" r="3"/><path d="M9 20a8 8 0 1 1 12 0"/><path d="M5 24a13 13 0 1 1 20 0"/></svg>
    </div><span class="cat-label">Internet</span></div>
    <div class="category"><div class="cat-icon" style="background:var(--amber)">
      <svg width="28" height="32" viewBox="0 0 28 32" fill="none" stroke="#fff" stroke-width="1.5"><path d="M9 20c-2-2-3-4-3-7a8 8 0 0 1 16 0c0 3-1 5-3 7v4H9z"/><line x1="10" y1="27" x2="18" y2="27"/><path d="M12 20l2-8 2 8"/><line x1="14" y1="0" x2="14" y2="2"/><line x1="3" y1="4" x2="5" y2="6"/><line x1="25" y1="4" x2="23" y2="6"/></svg>
    </div><span class="cat-label">Electricity</span></div>
    <div class="category"><div class="cat-icon" style="background:var(--sky)">
      <svg width="32" height="30" viewBox="0 0 32 30" fill="none" stroke="#fff" stroke-width="1.5"><path d="M2 14h16a6 6 0 0 1 6 6v2h-5v-2a2 2 0 0 0-2-2H2z"/><line x1="11" y1="14" x2="11" y2="8"/><line x1="6" y1="7" x2="16" y2="7"/><path d="M21 25c-1 2-2 3 0 4 2-1 1-2 0-4z"/></svg>
    </div><span class="cat-label">Water</span></div>
    <div class="category"><div class="cat-icon" style="background:var(--lime)">
      <svg width="24" height="32" viewBox="0 0 24 32" fill="none" stroke="#fff" stroke-width="1.5"><rect x="8" y="1" width="8" height="4"/><rect x="3" y="5" width="18" height="25" rx="4"/><line x1="3" y1="11" x2="21" y2="11"/><circle cx="12" cy="19" r="3"/><line x1="3" y1="25" x2="21" y2="25"/></svg>
    </div><span class="cat-label">Natural Gas</span></div>
  </div>

  <form class="search">
    <label class="search-label" for="inst">Search For Intitutions</label>
    <input id="inst" class="search-input" placeholder="Enter Institutions">
    <button type="button" class="search-btn">SEARCH</button>
  </form>
</main>

<footer class="site-footer">
  <div class="cards" role="img" aria-label="Accepted payment cards: Kartix, Odena, Pilsa, Norva">
    <span class="card"></span>
    <span class="card"></span>
    <span class="card"></span>
    <span class="card"></span>
  </div>
  <p class="copyright">©2017 Company Name. Terms of Use | Privacy</p>
</footer>
</body>
</html>
```